Soltravex business card

a nice business card with the logo,
Soltravex
Delia Vostrand
Marketing Director
CH-1296 Geneva
Switzerland
+41 79 612 3048
email: Delia.Vostrand@soltravex-mail.net

Target Market(s)

fertilizer business people, very nice and classic business card, normal size, make it nice and funky, try to make it different from the normal boring ones if possible.

Industry/Entity Type

Farming

Number of Pages Required

1 page

Requirements
Must have
• logo, Soltravex, my name - mail and phone number
regular business card size for me to print easy please

```html
<!DOCTYPE html>
<html lang="en">
<head>
<meta charset="utf-8">
<title>Soltravex business card</title>
<link href="https://fonts.googleapis.com/css2?family=Arimo:wght@400&display=swap" rel="stylesheet">
<style>
  :root {
    --leaf-green: #b0d235;
    --paper: #ffffff;
    --ink: #111111;
    --brand-grey: #666666;
  }
  html, body {
    margin: 0;
    padding: 0;
    width: 1200px;
    height: 805px;
    overflow: hidden;
    background: var(--paper);
  }
  .card {
    position: relative;
    width: 1200px;
    height: 805px;
    background: var(--paper);
    font-family: "Arimo", Arial, sans-serif;
    color: var(--ink);
    overflow: hidden;
  }
  .card__shapes {
    position: absolute;
    inset: 0;
    width: 100%;
    height: 100%;
  }
  .brand {
    position: absolute;
    left: 0;
    width: 470px;
    top: 528px;
    margin: 0;
    text-align: center;
    font-size: 29px;
    font-weight: 400;
    letter-spacing: 0.42em;
    text-transform: uppercase;
    color: var(--brand-grey);
    line-height: 1;
  }
  .person {
    position: absolute;
    left: 532px;
    top: 262px;
    margin: 0;
  }
  .person__name {
    margin: 0;
    font-size: 45px;
    font-weight: 400;
    line-height: 1.2;
    letter-spacing: 0.01em;
  }
  .person__role {
    margin: 4px 0 0;
    font-size: 36px;
    font-weight: 400;
    line-height: 1.2;
    letter-spacing: 0.06em;
  }
  .contact {
    position: absolute;
    left: 532px;
    top: 522px;
    margin: 0;
    font-style: normal;
    font-size: 29px;
    line-height: 44.6px;
  }
  .contact__line {
    display: block;
    white-space: nowrap;
  }
</style>
</head>
<body>
  <div class="card">
    <svg class="card__shapes" viewBox="0 0 1005 651" preserveAspectRatio="none" aria-hidden="true">
      <path class="card__panel" fill="var(--leaf-green)"
            d="M372,0 L1005,0 L1005,651 L332,651 C380,520 415,420 410,300 C406,190 392,90 372,0 Z"/>
      <path class="card__swoosh-line" fill="none" stroke="var(--leaf-green)" stroke-width="3"
            vector-effect="non-scaling-stroke"
            d="M295,0 C350,110 390,240 385,380 C382,490 362,580 338,632"/>
      <path class="card__wave-line" fill="none" stroke="var(--paper)" stroke-width="3"
            vector-effect="non-scaling-stroke"
            d="M335,640 C370,600 420,580 500,580 C620,580 760,608 870,620 C930,626 970,620 1005,605"/>
    </svg>

    <p class="brand">Soltravex</p>

    <div class="person">
      <h1 class="person__name">Delia VOSTRAND</h1>
      <p class="person__role">Marketing Director</p>
    </div>

    <address class="contact">
      <span class="contact__line">CH-1296 Geneva</span>
      <span class="contact__line">Switzerland</span>
      <span class="contact__line">tel: +41 79 612 3048</span>
      <span class="contact__line">e-mail: Delia.Vostrand@soltravex-mail.net</span>
    </address>
  </div>
</body>
</html>
```